Infographic for a Christian church discipleship pathway

We need to take a fairly complex program that helps people in a Baptist church follow Jesus, and turn it into a simple graphic. This graphic does not have to explain the whole program, web pages and print materials will do that. But, it should be something that people see and understand what it is quickly. The attached graphic is only to give the key words and general direction of the program. It should not serve as a design guide. In other words, we want to see some other ideas how this information can be imparted graphically with concision and creativity. It's important to note, the categories at the top (pray daily, read daily, gather weekly) are first steps, starting points....one shouldn't move forward until they've incorporated these things into their life. However, the categories that follow (study, connect, serve, etc) are not necessarily steps to take in sequential order.

The diagrams we've provided are not what we expect. They are only to explain the program. Here is a verbal description: The motto of our church is "A Ready Church" (ready to serve, ready to love, ready for when Jesus returns). There are four words that describe a ready church member: FOCUSED on the return of Christ, FAITHFUL in a daily relationship with Jesus, PREPARED for any opportunity to be a supernatural vessel of God's worK, LOOKING to invite others into God's family. The first two are God's Work in Me (Focused and faithful); the second two are God's Work Through me (Prepared, looking). Please use those two things as you wish (Focused faithful prepared looking; and God's word in and through me). If they are clarifying, please use. If not, you don't have to use.

Additionally, the strategies we employ to be "a ready church" are 1. Prayer 2. God's Word, and 3. Biblical Community. (So, in other words, these three things help us be a people who is focused, faithful, prepared, and looking....which is a ready church.

To provide some information how we will build this out: this graphic will be used in print and digital content. The digital content will allow people to click on each category to access training and resources associated with that discipline. (Fasting, reflecting, etc).

www.kwm.parish

Target Market(s)

35-50

Industry/Entity Type

Religious

Other font styles liked:
• Lato and/or Cambria

Requirements
Must have
• Fonts: lato, cambria. Colors#: 373E41, ebebe8, #a69677. Accent Colors: 80401D, #4e5730, #a5bac8
Nice to have
• A designer who has an understanding of what it means to incorporate the spiritual disciplines of the Christian faith into their life.

```html
<!DOCTYPE html>
<html lang="en">
<head>
<meta charset="utf-8">
<title>A Ready Church</title>
<link rel="stylesheet" href="https://fonts.googleapis.com/css2?family=Lato:ital,wght@0,300;0,400;0,700;0,900;1,400&family=Dancing+Script:wght@500&display=swap">
<style>
  :root {
    --charcoal: #373E41;
    --stone: #ebebe8;
    --tan: #a69677;
    --sky: #a5bac8;
    --sand: #f1e9dc;
    --band: #f0e6d6;
    --ring: #ddd3c3;
    --arc: #bdb6aa;
    --page: #f6f2f2;
    --white: #ffffff;
  }
  html, body {
    margin: 0;
    width: 1200px;
    height: 1200px;
    overflow: hidden;
    background: var(--page);
  }
  .poster {
    position: absolute;
    left: 187px;
    top: 16px;
    width: 826px;
    height: 1167px;
    display: block;
  }
  .title { font-family: "Lato", sans-serif; font-weight: 300; fill: var(--white); }
  .arc-title { font-family: "Lato", sans-serif; font-weight: 900; fill: var(--charcoal); letter-spacing: 1px; }
  .label { font-family: "Lato", sans-serif; font-weight: 700; fill: var(--charcoal); }
  .label-tan { font-family: "Lato", sans-serif; font-weight: 700; fill: var(--tan); }
  .label-white { font-family: "Lato", sans-serif; font-weight: 700; fill: var(--white); }
  .script { font-family: "Dancing Script", cursive; fill: var(--charcoal); }
  .credit { font-family: "Lato", sans-serif; font-style: italic; fill: #6b6b6b; }
  .tag-box { fill: var(--white); stroke: var(--tan); stroke-width: 1.5; }
  .dotted { fill: none; stroke: var(--tan); stroke-width: 1.5; stroke-dasharray: 2 2; }
  .step { fill: var(--sky); }
  .strategy-ring { fill: var(--white); stroke: var(--sky); stroke-width: 2; }
  .icon-slot { fill: #c7d4dd; }
</style>
</head>
<body>
<svg class="poster" viewBox="208 92 582 822" xmlns="http://www.w3.org/2000/svg">
  <defs>
    <path id="godsWorkArc" d="M 436 384 A 78 78 0 0 1 576 384"/>
    <clipPath id="medallionClip"><circle cx="506" cy="418" r="98"/></clipPath>
  </defs>

  <!-- Header -->
  <rect class="header-band" x="208" y="92" width="582" height="79" fill="var(--charcoal)"/>
  <text class="title" x="499" y="147" font-size="40" text-anchor="middle">A READY CHURCH</text>

  <!-- Body -->
  <rect class="body-panel" x="208" y="171" width="582" height="624" fill="var(--white)"/>

  <!-- Steeple -->
  <rect class="steeple" x="486" y="206" width="40" height="110" rx="4" fill="#d9cfbf" role="img" aria-label="Church steeple with cross"/>

  <!-- Medallion -->
  <g class="medallion">
    <circle cx="506" cy="418" r="100" fill="var(--sand)" stroke="var(--ring)" stroke-width="5"/>
    <g clip-path="url(#medallionClip)">
      <rect x="396" y="473" width="220" height="60" fill="var(--charcoal)"/>
    </g>
    <text class="arc-title" font-size="20"><textPath href="#godsWorkArc" startOffset="50%" text-anchor="middle">GOD'S WORK</textPath></text>
    <rect class="people-pair" x="448" y="386" width="118" height="58" rx="6" fill="#e6cdb4" role="img" aria-label="Two church members, one with hands on heart, one holding a heart"/>
    <rect class="tag-box" x="427" y="446" width="78" height="24" rx="2"/>
    <text class="label" x="466" y="463" font-size="12.5" text-anchor="middle">FOCUSED</text>
    <rect class="tag-box" x="507" y="446" width="80" height="24" rx="2"/>
    <text class="label" x="547" y="463" font-size="12.5" text-anchor="middle">FAITHFUL</text>
    <text class="label-white" x="506" y="498" font-size="16" text-anchor="middle">IN ME</text>
  </g>

  <!-- Through me, left -->
  <text class="label-tan" x="336" y="408" font-size="13.5" text-anchor="middle">THROUGH ME</text>
  <path class="dotted" d="M 405 415 H 337 V 446"/>
  <rect class="tag-box" x="292" y="447" width="82" height="24" rx="2"/>
  <text class="label" x="333" y="464" font-size="12.5" text-anchor="middle">PREPARED</text>

  <!-- Through me, right -->
  <text class="label-tan" x="676" y="408" font-size="13.5" text-anchor="middle">THROUGH ME</text>
  <path class="dotted" d="M 608 415 H 672 V 446"/>
  <rect class="tag-box" x="631" y="447" width="75" height="24" rx="2"/>
  <text class="label" x="668" y="464" font-size="12.5" text-anchor="middle">LOOKING</text>

  <!-- Arcs -->
  <path d="M 275 499 Q 497 820 717 501" fill="none" stroke="var(--arc)" stroke-width="1.5"/>
  <path d="M 336 499 Q 500 690 662 501" fill="none" stroke="var(--sky)" stroke-width="1.5"/>
  <circle cx="275" cy="499" r="5" fill="var(--charcoal)"/>
  <circle cx="336" cy="499" r="5" fill="var(--charcoal)"/>
  <circle cx="662" cy="501" r="5" fill="var(--charcoal)"/>
  <circle cx="717" cy="501" r="5" fill="var(--charcoal)"/>

  <!-- First steps -->
  <text class="script" x="500" y="552" font-size="22" text-anchor="middle">First Steps</text>
  <circle class="step" cx="396" cy="565" r="33"/>
  <text class="label-white" x="396" y="562" font-size="12" text-anchor="middle">PRAY</text>
  <text class="label-white" x="396" y="576" font-size="12" text-anchor="middle">DAILY</text>
  <circle class="step" cx="500" cy="597" r="33"/>
  <text class="label-white" x="500" y="595" font-size="12" text-anchor="middle">READ</text>
  <text class="label-white" x="500" y="609" font-size="12" text-anchor="middle">DAILY</text>
  <circle class="step" cx="605" cy="565" r="33"/>
  <text class="label-white" x="605" y="562" font-size="12" text-anchor="middle">GATHER</text>
  <text class="label-white" x="605" y="576" font-size="12" text-anchor="middle">WEEKLY</text>

  <!-- Strategy -->
  <text class="label" x="500" y="652" font-size="16" text-anchor="middle">OUR STRATEGY</text>

  <circle class="strategy-ring" cx="335" cy="650" r="34"/>
  <rect class="icon-slot" x="317" y="630" width="36" height="40" rx="8" role="img" aria-label="Praying hands icon"/>
  <text class="label" x="335" y="702" font-size="12.5" text-anchor="middle">PRAYER</text>

  <circle class="strategy-ring" cx="500" cy="703" r="34"/>
  <rect class="icon-slot" x="484" y="684" width="32" height="40" rx="3" role="img" aria-label="Bible with cross icon"/>
  <text class="label" x="500" y="755" font-size="12.5" text-anchor="middle">GOD'S WORD</text>

  <circle class="strategy-ring" cx="660" cy="651" r="34"/>
  <rect class="icon-slot" x="638" y="633" width="44" height="36" rx="8" role="img" aria-label="Gathered community icon"/>
  <text class="label" x="660" y="705" font-size="12.5" text-anchor="middle">BIBLICAL</text>
  <text class="label" x="660" y="720" font-size="12.5" text-anchor="middle">COMMUNITY</text>

  <text class="credit" x="778" y="792" font-size="7" text-anchor="end">Icons by Pixelwell from Glyphhub.net</text>

  <!-- Footer -->
  <rect x="208" y="795" width="582" height="83" fill="var(--band)"/>
  <rect class="crowd" x="362" y="806" width="268" height="72" rx="4" fill="#d8c3a8" role="img" aria-label="Group of diverse church members praying, worshipping and celebrating"/>
  <rect x="208" y="878" width="582" height="36" fill="var(--tan)"/>
  <text class="label-white" x="499" y="902" font-size="15.5" font-weight="400" text-anchor="middle" letter-spacing="0.3">HELPS PEOPLE IN A BAPTIST CHURCH FOLLOW JESUS</text>
</svg>
</body>
</html>
```